Web Design with a Twist! Not cheap design

Please note that this project is ending at 5pm on Tuesday the 28th of September, Australian Western Standard Time!!

Please also note that this project has now been guaranteed!

This project involves three primary elements:
* Logo design;
* Web design - of additional pages and page elements to fit into a site that is already in design/development;
* Graphic design - various images used on the site.

The following materials are included for the project:
* Project requirements
* Company / Site name
* Company / Site description
* Wireframes for new pages / page elements
* Screenshots of existing designs and accompanying definition of constraints for new designs
* PSDs for existing site designs
* Technical requirements for designs
* Content (to guide designs)

Project Requirements:

* Logo design:
This is a new company / site, so we need a new logo. We want to see what you come up with here without giving too much direction that may restrict creativity. If desired, you may find possible guidance through considering the company name, company description, and the existing site designs. Please note that the current logo in the site is for placeholder purposes only.

* Web design:
We need the following pages (and features) to be designed for the site:
• Home page
• Advertise page
• How it works page
We’ve provided some wireframes for the pages, however we definitely don't want you to be guided by the layout/styling at all - the wireframes are only there to indicate the features that we require on each page only. So please ignore all aspects of the wireframes except for the indications of features and functionality.

* Graphic design:
We need various images to be designed throughout the site. These include:
• The image at the top of the ‘Home’ page – please note we will provide some direction on this asap
• The image at the top of the ‘Advertise’ page – please note we will provide some direction n this asap
• The image at the top of the ‘How it Works’ pages
• The images that accompany each of the left hand menu items on the ‘How it Works’ pages (the main images & thumbnails if that’s part of your design). Please note that these images need to be constructed to match the Headlines for each of the ‘What’, ‘Who’, ‘Where’, etc menu items. These Headlines (and some descriptive text) can be found in the Content section at the end of this brief.
• The map of Australia for the ‘Home’ page
• The images to accompany the pricing section of the ‘Advertise’ page
• The variations of the ‘Life in the search lane’ images that are used on the ‘Home’, ‘Advertise’, and ‘How it Works’ pages. Please note that if you want to use different imagery (or no imagery, dependent upon your design) for the Home and Advertise pages then this is your call.

Company Name:
TaskBloom

Company / Site description:
This site will provide a means for contractors ('advertisers') to easily specify and advertise their services, coupled with a means for employers (‘buyers’) to easily seek out and contact these people.
The site will cater for contractor-side advertisements only; job postings will not be accommodated (turning the traditional job advertisement model on its head).
In general, the functionality of the site is somewhat like a mashup of sites like crewvault.com and stayvane.com. The site will incorporate the following primary features of contractor profile display and search, company profile display, (and an availability calendar for v2 release).

Constraints for designs:
On some of the existing designs you will notice that a number of the elements of the site have already been designed. When constructing your designs, please work in accordance with the following constraints:

You have to keep:
• Colour scheme in the header
• Colour scheme in the top navigation buttons (including text colour and background colour)
• Colour scheme for the buttons like on the Register page

You can ignore:
• The existing placeholder logo
• Border, layout, and colour scheme for page elements (like the lines around and inside the register section on the Register page)
• Design of text fields
• Font colour scheme throughout the site – the orange and grey headlines and body text
• Design and colour scheme of the map of Australia
• The breadcrumbs (whether or not they appear, and their layout, styling, colour scheme etc)
• Dropdown styling (assuming you had to make some; currently not on any pages we’re asking you to do) like on the Browse Profession page
• Profile styling (for the home page featured profiles) like on the Browse Profession page
• Footer styling
• Anything else we haven’t explicitly asked you to keep

Technical requirements for design:
Any site designs in either Layered Pixform files (PSD's) or Illustrator Drawings (AI). RGB Color. Must fit current site design, we work to 1024 wide screens. Usuable area is defined in site designs that are attached in the Pixform documents; it's around 960px.
Logo work needs to be Illustrator Drawings (AI) and EPS. Need CMYK images for printing and RGB for screen. Logos must include any special fonts that are used as TTF or Open Type. Logos need Color, Monochrome, Reversed and both Tall and Wide usages.

Content for the 'How it Works' pages - this content should guide the images that appear on each page.
* What
Headline: TaskBloom brings contractors and employers together
Descriptive text: (turns the traditional job search model on its head)
* Who
Headline: TaskBloom is for highly skilled professionals and fast moving companies
Descriptive text:
* Where
Headline: Anywhere in Australia, TaskBloom is working by your side
Descriptive text:
* Why
Headline: There are more than 1 million reasons to love TaskBloom
Descriptive text: In Australia, there are 1 million people who work as contractors in their main job, and a further 100,000 people who are contractors in their second job. That’s a lot of contractors!
* When
Headline: TaskBloom is forming partnerships 24 hours a day
Descriptive text:
* How
Headline: Life in the search lane, with TaskBloom
Descriptive text: Advertise on TaskBloom now, and get your life in the search lane.

Remember
Just remember the wireframes we have submitted are just a guide – we want to see your creativity shine. And above all else - have fun!
Thank you.
Updates

Please note the deadline for this design competition 5pm on Tuesday the 28th of September, Australian Western Standard Time.

Just under 3 days away!

The deadline of the project will soon be updated to reflect this.

Hi Designers!

Just to be 100% clear about the deadline - the timer is currently showing 7 hours too many. In other words, the project will end 7 hours before the timer finishes.

I will send a notification if the timer starts to display the correct time. So until then, please remember that the deadline is earlier than it seems!

Thanks

Hi Designers,

A couple of really important points:

Firstly - if everyone could please stick to the theme that we provided in the Pixform files that would be excellent. It is not possible for us to create a new theme. We're dealing with very tight deadlines, so please just provide designs that fit within the current theme.

Secondly, we were really hoping for more illustrations / graphics to be provided in the designs. We're not a fan of the stock photos of generic business people. So please send through designs that incorporate illustrations / graphics for any imagery.

Also just a reminder that this competition is still ending 7 hours earlier than the timer currently displays.

Thanks.

Target Market(s)

The ‘advertiser’ target market for the site is white collar professionals, in all types of industries. The site will be catering for premium contractors only. The site will be catering for both 'in person' contractors, as well as 'knowledge economy' contractors. The site will not be seeking to compete with gigmora.com, plixo.com, taskrune.com, or similar sites.

The advertiser target market will also encompass companies and labour hire agencies that have contractors in their workforce.

The ‘buyer’ target market will encompass employers, recruitment agents, and member-to-member hiring.

Industry/Entity Type

Contractor

Requirements
Must have
• As per overview
Nice to have
• As per overview
Should not have
• As per overview

```html
<!DOCTYPE html>
<html lang="en">
<head>
<meta charset="utf-8">
<title>TaskBloom</title>
<link href="https://fonts.googleapis.com/css2?family=Arimo:wght@400;700&family=PT+Sans+Narrow:wght@400;700&family=Open+Sans:wght@700&display=swap" rel="stylesheet">
<style>
:root{
  --header:#5f7088;
  --header-dark:#55657b;
  --tab:#a4afbd;
  --tab-text:#e9edf2;
  --orange:#ff5a00;
  --accent:#f26522;
  --red:#c8321a;
  --ink:#38414e;
  --body:#55595e;
  --page:#f3f4f4;
  --panel:#eef4f4;
  --line:#d6dcdf;
  --footer:#3e4a5b;
  --footer-text:#8795a6;
}
*{margin:0;padding:0;box-sizing:border-box}
html,body{width:1200px;height:1090px;overflow:hidden}
body{position:relative;background:var(--page);font-family:Arimo,Arial,sans-serif;color:var(--body)}
.abs{position:absolute}
.header{left:0;top:0;width:1200px;height:119px;background:linear-gradient(var(--header-dark),var(--header))}
.logo{left:130px;top:0;width:141px;height:153px}
.logo-name{left:130px;top:106px;width:141px;text-align:center;color:#fff;font:700 19px "Open Sans",sans-serif;letter-spacing:.3px}
.nav{left:335px;top:92px;display:flex;gap:6px}
.nav a{display:block;height:27px;line-height:28px;padding:0 15px;background:var(--tab);color:var(--tab-text);border-radius:8px 8px 0 0;font:700 15px "Open Sans",sans-serif;text-decoration:none}
.nav a.home{background:#fff;width:43px;padding:0;display:flex;align-items:center;justify-content:center}
.search{left:831px;top:134px;width:249px;height:27px;display:flex}
.search .field{flex:1;border:1px solid #cfd4d8;background:#fff;border-radius:3px 0 0 3px;display:flex;align-items:center;gap:6px;padding-left:8px;font-size:14px;color:#7d8690}
.search .go{width:41px;background:#7a889a;color:#fff;font:700 13px Arimo,sans-serif;display:flex;align-items:center;justify-content:center;border-radius:0 3px 3px 0}
.hero{left:130px;top:177px;width:960px;height:365px;background:#fff;border:1px solid #e1e4e6}
.hero h1{left:21px;top:52px;font:700 33px "PT Sans Narrow",sans-serif;color:var(--ink);white-space:nowrap}
.hero h1 em{font-style:normal;color:var(--orange)}
.hero p{left:40px;top:109px;width:490px;text-align:center;font-size:14.5px;line-height:22px;color:#5f6873}
.hero p b{color:var(--ink)}
.btn-grey{left:226px;top:194px;width:114px;height:32px;border-radius:16px;background:linear-gradient(#fafafa,#d9d9d9);border:1px solid #c6c6c6;box-shadow:0 1px 2px rgba(0,0,0,.2);font:700 13px Arimo,sans-serif;color:#444;text-align:center;line-height:30px}
.hero-art{left:560px;top:20px;width:350px;height:265px;border-radius:40%;background:radial-gradient(ellipse at center,#eceef0 0%,#f6f7f8 55%,#fff 75%)}
.finder{left:7px;top:287px;width:945px;height:69px;background:#ebebeb}
.finder .avatar{left:16px;top:8px;width:48px;height:54px;border-radius:24px 24px 4px 4px;background:linear-gradient(#5a5a5a,#2a2a2a)}
.finder h2{left:75px;top:21px;font:700 23px "PT Sans Narrow",sans-serif;color:#2f3640;white-space:nowrap}
.input{height:28px;border:1px solid #cfd3d6;background:#fff;font-size:12px;color:#8a9099;padding:6px 14px;letter-spacing:.3px}
.kw{left:382px;top:22px;width:199px}
.state{left:598px;top:23px;width:152px;height:26px;padding:5px 10px}
.state .arr{position:absolute;right:4px;top:5px;width:15px;height:15px;border:1px solid #999;background:#f3f3f3}
.btn-orange{height:28px;border-radius:3px;background:linear-gradient(#ff7a52,#f2512a);color:#fff;font:700 14px Arimo,sans-serif;text-align:center;line-height:28px}
.finder .btn-orange{left:769px;top:23px;width:144px}
.panel{background:var(--panel);border:1px solid var(--line);border-radius:6px 6px 0 0}
.panel-head{height:36px;background:linear-gradient(#6b7b8f,#4e5d71);border-radius:5px 5px 0 0;color:#fff;font:700 17px Arimo,sans-serif;line-height:34px;padding-left:19px}
.about{left:131px;top:557px;width:625px;height:339px}
.about .intro{padding:12px 19px 0;font-size:11px;line-height:20px}
.about strong{display:block;font-size:12.5px;color:#3e444b;line-height:14px;margin-bottom:5px}
.list{list-style:none;padding:9px 0 0 80px}
.list li{position:relative;font-size:11px;line-height:20px;margin-bottom:12px}
.list li strong{margin-bottom:2px}
.list li svg{position:absolute;left:-32px;top:2px}
.readmore{right:25px;bottom:17px;font:700 11px Arimo,sans-serif;color:var(--red)}
.how{left:131px;top:910px;width:625px;height:56px;background:#cde5e7;border:1px solid #b9d2d5}
.how h3{left:81px;top:14px;font:700 20px Arimo,sans-serif;color:var(--ink);white-space:nowrap}
.how h3 span{color:var(--red)}
.featured{left:771px;top:557px;width:318px;height:409px}
.profile{position:relative;height:116px;border-bottom:1px solid #dde3e4}
.photo{left:18px;top:9px;width:76px;height:81px;border:2px solid #fff;outline:1px solid #c9cfd2;background:linear-gradient(#c9d7e4,#9fb1c2)}
.profile .txt{left:103px;top:12px;width:210px;font-size:11px;line-height:14px;color:#4b5057}
.profile .name{color:var(--red);font-weight:700;font-size:12.5px;display:block;margin-bottom:5px}
.profile .role{color:#333;font-weight:700;font-size:12.5px;display:block;margin-bottom:5px}
.featured .btn-orange{left:135px;top:368px;width:144px}
.footer{left:0;top:982px;width:1200px;height:108px;background:var(--footer);box-shadow:inset 0 6px 8px rgba(0,0,0,.25)}
.fcol{top:18px;font-size:12px;line-height:20px;color:var(--footer-text)}
.fcol b{display:block;color:#aab5c2;font-size:12.5px}
.follow{left:917px;top:37px;font:700 12px Arimo,sans-serif;color:var(--footer-text);display:flex;align-items:center;gap:7px}
.follow i{display:inline-block;width:15px;height:15px;border-radius:2px;background:#6f8fc0}
.copy{left:832px;top:75px;font-size:11.5px;color:var(--footer-text)}
</style>
</head>
<body>
<div class="abs header"></div>
<svg class="abs logo" viewBox="0 0 141 153" aria-hidden="true">
  <path d="M0 0H141V146l-4 7-4-7-4 7-4-7-4 7-4-7-4 7-4-7-4 7-4-7-4 7-4-7-4 7-4-7-4 7-4-7-4 7-4-7-4 7-4-7-4 7-4-7-4 7-4-7-4 7-4-7-4 7-4-7-4 7-4-7-4 7-4-7-4 7-4-7-4 7-4-7-4 7-4-7-4 7-4-7-4 7-4-7-4 7-4-7Z" fill="var(--orange)"/>
  <circle cx="70" cy="68" r="16" fill="#fff"/>
</svg>
<div class="abs logo-name">TASKBLOOM</div>
<nav class="abs nav">
  <a class="home" href="#" aria-label="Home"><svg width="14" height="13" viewBox="0 0 14 13"><path d="M7 0 0 6h2v7h4V9h2v4h4V6h2Z" fill="#9aa6b4"/></svg></a>
  <a href="#">FIND</a><a href="#">ADVERTISE</a><a href="#">HOW IT WORKS</a><a href="#">BLOG</a><a href="#">LOGIN</a><a href="#">REGISTER</a>
</nav>
<div class="abs search">
  <div class="field"><svg width="16" height="16" viewBox="0 0 16 16"><circle cx="6.5" cy="6.5" r="5" fill="none" stroke="#9aa6b4" stroke-width="2"/><path d="M10 10l5 5" stroke="#9aa6b4" stroke-width="2.5"/></svg>Find a contractor</div>
  <div class="go">Go</div>
</div>

<section class="abs hero">
  <h1 class="abs">We brings <em>contractors</em> &amp; <em>employers</em> together</h1>
  <p class="abs"><b>TASKBLOOM</b> will provide a means for contractors ('advertisers') to easily specify and advertise their services, coupled with a means for employers (‘buyers’) to easily seek out and contact these people.</p>
  <div class="abs btn-grey">Resigter Now!</div>
  <div class="abs hero-art" role="img" aria-label="Illustration of a map of Australia with figures standing across it, two highlighted in orange on targets"></div>
  <div class="abs finder">
    <div class="abs avatar" role="img" aria-label="Illustration of a professional in a suit"></div>
    <h2 class="abs">Find Highly Skilled Professionals:</h2>
    <div class="abs input kw">Type Keywords</div>
    <div class="abs input state">Select State<span class="arr"></span></div>
    <div class="abs btn-orange">Find Contractors</div>
  </div>
</section>

<section class="abs panel about">
  <div class="panel-head">About TaskBloom</div>
  <div class="intro"><strong>Sed gravida commodo lacus sed faucibus.</strong>Donec et nibh mauris. In lobortis massa quis nibh varius at euismod risus eleifend. Maecenas id mi ante. Morbi adipiscing molestie convallis. Morbi est metus, porttitor quis fermentum laoreet, aliquam ut arcu. Curabitur eget lacus at nisl bibendum hendrerit ac nec nulla. Pellentesque at elit eu leo mattis eleifend quis ac urna.</div>
  <ul class="list">
    <li><svg width="18" height="14" viewBox="0 0 18 14"><path d="M1 8l5 4L17 2" fill="none" stroke="var(--accent)" stroke-width="3"/></svg><strong>Sed gravida commodo lacus sed faucibus.</strong>Donec et nibh mauris. In lobortis massa quis nibh varius at euismod risus eleifend.</li>
    <li><svg width="18" height="14" viewBox="0 0 18 14"><path d="M1 8l5 4L17 2" fill="none" stroke="var(--accent)" stroke-width="3"/></svg><strong>Sed gravida commodo lacus sed faucibus.</strong>Donec et nibh mauris. In lobortis massa quis nibh varius at euismod risus eleifend. Donec et nibh mauris. In lobortis massa quis nibh varius at euismod risus eleifend.</li>
    <li><svg width="18" height="14" viewBox="0 0 18 14"><path d="M1 8l5 4L17 2" fill="none" stroke="var(--accent)" stroke-width="3"/></svg><strong>Sed gravida commodo lacus sed faucibus.</strong>Donec et nibh mauris. In lobortis massa quis nibh varius at euismod risus eleifend.</li>
  </ul>
  <a class="abs readmore">Read More »</a>
</section>

<section class="abs how">
  <svg class="abs" style="left:18px;top:8px" width="54" height="40" viewBox="0 0 54 40"><path d="M2 2h34v26l16 10H2Z" fill="#f7fafa" stroke="#9fb4b8"/><text x="19" y="27" text-anchor="middle" font-family="Arimo,sans-serif" font-weight="700" font-size="22" fill="#4d5866">?</text></svg>
  <h3 class="abs">How it Works - “<span>Life in the Search Lane?</span>”</h3>
</section>

<section class="abs panel featured">
  <div class="panel-head">Featured Profile</div>
  <div class="profile"><div class="abs photo" role="img" aria-label="Portrait photo of the featured contractor"></div><div class="abs txt"><span class="name">Milo Ashcombe</span><span class="role">Designer, Developer, Producer</span>Scriptel, Pixform, CoreWeb, Project Management, Editorial, Photography, Consultancy</div></div>
  <div class="profile"><div class="abs photo" role="img" aria-label="Portrait photo of the featured contractor"></div><div class="abs txt"><span class="name">Owen Darcy</span><span class="role">Consultant, Developer</span>Scriptel, Pixform, CoreWeb, Project Management</div></div>
  <div class="profile" style="border:0"><div class="abs photo" role="img" aria-label="Portrait photo of the featured contractor"></div><div class="abs txt"><span class="name">Lenny Marsh</span><span class="role">Designer, Developer, Producer</span>Servicing New South Wales, Victoria and New South Wales</div></div>
  <div class="abs btn-orange">Find Contractors</div>
</section>

<footer class="abs footer">
  <div class="abs fcol" style="left:130px"><b>About us</b>Features<br>Pricing<br>Team</div>
  <div class="abs fcol" style="left:242px"><b>Support</b>Contact us<br>FAQ</div>
  <div class="abs fcol" style="left:360px"><b>Browse</b>By state<br>Business</div>
  <div class="abs fcol" style="left:470px"><b>Legal</b>Privacy Policy<br>Terms &amp; Conditions</div>
  <div class="abs follow">Follow us on: <i></i><i></i><i style="background:#5bb8e6"></i></div>
  <div class="abs copy">© Copyright 2010 TaskBloom. Al right reserved.</div>
</footer>
</body>
</html>
```